Logo and Card design for KRV Home Solutions LLC

I need an edgier logo and business card designs. Current logo attached. I like the colors below. I would like the logo to incorporate a home in the design.
Title = Principal-Acquisitions
Email:KRVHOMESOLUTIONS@mailnest.example
555-014-2739
facebook
IG
2 sided business card with the front being contact info a slogan about selling a home fast. The back incorporating What we do. Buy houses, land, or commercial property as is. We find solutions to make the process of selling simple and fair.

Target Market(s)

Motivated house sellers.

Industry/Entity Type

Business

Contact Information for Business Card

Who we are: We are a Faith based Real Estate Investment Company. We pay cash for homes in any condition and can close quick. Whatever the reason you need to sell fast, we can help. We believe in creating win-win solutions to help you in your time of need. We care! We can help!

Logo Text

KRV Home Solutions LLC

Font styles to use
Sans Serif

Colors
33a6d7
0355a3
85abd2
cee9f5
9d9d9d
b2b2b2
ffffff

Requirements
Must have
• Old logo attached. I want something edgier.
• Company name, phone number, description on the back of what we can do. Pay all cash. Buy in as is condition. No fees,Commisions or closing costs.Close quick. No hassles with solutions to meet your unique situation.
• Call today for an offer within 24 hours.

```html
<!DOCTYPE html>
<html lang="en">
<head>
<meta charset="utf-8">
<title>KRV Home Solutions – Business Card</title>
<link rel="stylesheet" href="https://fonts.googleapis.com/css2?family=Roboto:wght@400;500;700&family=Roboto+Condensed:wght@400;500;700&display=swap">
<style>
  :root {
    --navy: #1f3a6e;
    --grey-text: #555a60;
    --stage: #2b2b2b;
    --paper: #f2f2f2;
    --white: #ffffff;
    --sky-top: #dfeaf3;
    --sky-mid: #c9d9e4;
    --leaf: #b9cbb0;
  }
  * { margin: 0; padding: 0; box-sizing: border-box; }
  html, body { width: 1200px; height: 960px; overflow: hidden; }
  body { background: var(--stage); position: relative; font-family: "Roboto", Arial, sans-serif; }

  .card { position: absolute; width: 600px; height: 343px; overflow: hidden; box-shadow: 0 4px 10px rgba(0,0,0,.45); }
  .card--front { left: 314px; top: 113px; }
  .card--back { left: 311px; top: 472px; background: var(--paper); }

  .front__photo { position: absolute; inset: 0; background: linear-gradient(120deg, var(--sky-top) 0%, var(--sky-mid) 55%, var(--leaf) 100%); }
  .front__band { position: absolute; inset: 0; }

  .brand { position: absolute; font-family: "Roboto", Arial, sans-serif; font-weight: 500; color: var(--navy); white-space: nowrap; display: flex; align-items: center; gap: 8px; line-height: 1; }
  .brand__square { width: 10px; height: 10px; background: var(--navy); flex: none; }
  .card--front .brand { right: 32px; top: 80px; font-size: 17px; }
  .card--back .brand { left: 0; right: 0; top: 100px; font-size: 22px; justify-content: center; }

  .contact { position: absolute; left: 31px; top: 140px; color: var(--white); }
  .contact__name { font-weight: 500; font-size: 23px; letter-spacing: .2px; line-height: 28px; }
  .contact__title { font-weight: 500; font-size: 15px; line-height: 20px; margin-bottom: 5px; }
  .contact__list { list-style: none; font-size: 14.5px; line-height: 19.5px; }
  .contact__list li { display: flex; align-items: center; gap: 8px; }
  .contact__list svg { width: 14px; height: 14px; fill: var(--white); flex: none; }
  .slogan { margin-top: 6px; font-family: "Roboto Condensed", "Arial Narrow", sans-serif; font-size: 14.5px; line-height: 18px; }

  .about { position: absolute; left: 0; right: 0; top: 169px; text-align: center; color: var(--grey-text); font-size: 15.2px; line-height: 18px; }
  .about__heading { color: var(--navy); font-weight: 700; font-size: 15.5px; line-height: 20px; }
  .about__text + .about__heading { margin-top: 12px; }
</style>
</head>
<body>

<section class="card card--front">
  <div class="front__photo" role="img" aria-label="Soft background photograph of a house with trees"></div>
  <svg class="front__band" viewBox="0 0 600 343" aria-hidden="true">
    <polygon fill="var(--navy)" points="0,118 300,118 525,343 0,343"/>
  </svg>

  <div class="brand"><span class="brand__square"></span><span>KRV Home Solutions LLC</span></div>

  <div class="contact">
    <h1 class="contact__name">MARCUS REED</h1>
    <p class="contact__title">Principal-Acquisitions</p>
    <ul class="contact__list">
      <li><svg viewBox="0 0 24 24"><path d="M6.6 10.8a15.2 15.2 0 0 0 6.6 6.6l2.2-2.2a1 1 0 0 1 1-.25 11.4 11.4 0 0 0 3.6.57 1 1 0 0 1 1 1V20a1 1 0 0 1-1 1A17 17 0 0 1 3 4a1 1 0 0 1 1-1h3.5a1 1 0 0 1 1 1c0 1.25.2 2.45.57 3.57a1 1 0 0 1-.25 1z"/></svg>555-014-2739</li>
      <li><svg viewBox="0 0 24 24"><path d="M3 5h18v14H3zM4.5 6.5v.6L12 12l7.5-4.9v-.6z"/></svg>KRVHOMESOLUTIONS@mailnest.example</li>
      <li><svg viewBox="0 0 24 24"><path d="M12 2a10 10 0 1 0 0 20 10 10 0 0 0 0-20zm-1 17.9A8 8 0 0 1 4.1 10.9L9 15.8v1a2 2 0 0 0 2 2zm6.9-2.5A2 2 0 0 0 16 16h-1v-3a1 1 0 0 0-1-1H8v-2h2a1 1 0 0 0 1-1V7h2a2 2 0 0 0 2-2v-.4a8 8 0 0 1 2.9 12.8z"/></svg>KRVHOMESOLUTIONS.example</li>
    </ul>
    <p class="slogan">Pay all cash. Buy in as is condition.<br>No fees,Commisions or closing costs.Close quick.<br>No hassles with solutions to meet your unique situation.<br>Call today for an offer within 24 hours.</p>
  </div>
</section>

<section class="card card--back">
  <div class="brand"><span class="brand__square"></span><span>KRV Home Solutions LLC</span></div>
  <div class="about">
    <h2 class="about__heading">WHO WE ARE</h2>
    <p class="about__text">We are a Faith based Real Estate Investment Company. We pay cash for<br>homes in any condition and can close quick. Whatever the reason you need<br>to sell fast, we can help. We believe in creating win-win solutions to help</p>
    <h2 class="about__heading">WHAT WE DO</h2>
    <p class="about__text">Buy houses, land, or commercial property as is.<br>We find solutions to make the process of selling simple and fair.</p>
  </div>
</section>

</body>
</html>
```